Ridgeway Pack Outfitters Needs a Brochure Design

We are looking for a tri-fold brochure design that we can use for a direct mail advertising campaign. We provide guide services to big game hunters in the state of New Mexico. We would like to see designs that utilize our company logo and several of our photos from our website (www.highmesaguides.example). Our clientele like eye candy and we want to show off our past customers success through our great field photos. The final design should communicate our services, various hunts, and pricing. Below is a rough concept of the pertinent info we would like included:

Front Cover - Company logo, website address, Phone Number, Web Pic 46 from below files, Below picture text "Turning dreams into reality, one trophy at a time!", centered on very bottom "New Mexico's Premier Outfitter"

Inside Left - Elk pic 3 on top 1/3rd, "Welcome To....." text box down to bottom 1/3rd, web pic 10 on the bottom of the panel

Inside Center - "New Mexico Elk Hunting" Title
Fully Outfitted Elk Hunts - 5-6 sentences describing hunt and what services are included
Rates - List going down the panel the various hunts and pricing (ex Early Season Archery Bull Elk $3,500)
Web Pic 43 centered lower portion of panel

Inside Right - "Other Hunts"
Barbary Sheep Rates and Days
Mule Deer Rates and Days
Turkey Rates and Days
Text " Above hunts include guide service, lodging, etc"
Web pics 56 incorporated into this panel

Inside Flap - "Youth Hunts"
Text decribing youth hunting opportunities and special discount pricing
Youth Elk Rate
Youth Mule Deer Rate
Youth Turkey Rate
Include any combo of web pics 14,22, 17

Back - Text saying "Give us a call before the draw deadline to book the best hunt of your life!" contact info, room for necessary mailing indica, postage, and mailing address

Target Market(s)

Recreational outdoor/hunting enthusiasts

Industry/Entity Type

Advertising

Requirements
Must have
• Applies to Back Panel Only - Please be sure your design allows 1.00" from the edges at the top right corner so that we can place an indicia for mailing. Also, please leave 2.25" x 4.25" of white space in the bottom right corner for inkjetting of addresses.

```html
<!DOCTYPE html>
<html lang="en">
<head>
<meta charset="utf-8">
<title>Ridgeway Pack Outfitters – Tri-fold Mailer</title>
<link href="https://fonts.googleapis.com/css2?family=Open+Sans:ital,wght@0,400;0,600;0,700;1,600;1,700&family=Roboto+Condensed:wght@700&display=swap" rel="stylesheet">
<style>
  :root{
    --board:#c89a68;
    --wood-dark:#141414;
    --wood-mid:#2e2e2e;
    --white:#ffffff;
    --red:#e3232b;
    --ink:#111111;
    --photo-green:#6f7a52;
    --photo-brown:#7a6148;
    --photo-sky:#9fb0b8;
  }
  *{box-sizing:border-box;margin:0;padding:0}
  html,body{width:1200px;height:955px;overflow:hidden}
  body{background:var(--board);font-family:"Open Sans",Arial,sans-serif;position:relative}

  .panel-label{position:absolute;top:38px;color:var(--white);font:700 27px "Open Sans",Arial,sans-serif;width:200px;text-align:center}

  .brochure{position:absolute;left:95px;top:93px;width:1012px;height:788px;box-shadow:0 4px 10px rgba(0,0,0,.45);
    background:linear-gradient(90deg,var(--wood-dark),var(--wood-mid) 20%,var(--wood-dark) 40%,var(--wood-mid) 62%,var(--wood-dark) 80%,var(--wood-mid));}
  .panel{position:absolute;top:0;height:100%;border-right:1px solid #000}
  .panel--flap{left:0;width:348px}
  .panel--back{left:348px;width:321px;z-index:2}
  .panel--front{left:669px;width:343px;border-right:none;z-index:1}

  /* Back flap */
  .youth-title{position:absolute;top:30px;width:100%;text-align:center;color:var(--white);font-weight:700;font-size:19px}
  .youth-sub{position:absolute;top:63px;width:100%;text-align:center;color:var(--white);font-size:11px}
  .youth-price{position:absolute;top:78px;width:100%;text-align:center;color:var(--white);font-weight:700;font-size:19px}
  .youth-copy{position:absolute;top:116px;left:45px;width:263px;color:var(--white);font-size:10.6px;line-height:1.36;text-align:justify}
  .rates{position:absolute;top:256px;left:45px;width:265px;color:var(--white);font-size:10.6px}
  .rate{display:flex;margin-bottom:9px}
  .rate dt{width:120px;flex:none}
  .rate dd{flex:1;font-size:12px;line-height:1.45}
  .rate dd p{padding-left:11px;text-indent:-11px}
  .photo-strip{position:absolute;top:423px;left:0;width:348px;height:246px;background:var(--red);padding:5px 0}
  .photo{position:absolute}
  .photo--turkey{left:0;top:5px;width:168px;height:236px;background:linear-gradient(160deg,var(--photo-green),#4b3f33 70%,#6b5c48)}
  .photo--youth-elk{left:172px;top:5px;width:176px;height:236px;background:linear-gradient(180deg,#3d4a2e,#6a6a48 55%,#8a7a5a)}
  .connect-title{position:absolute;top:690px;width:100%;text-align:center;color:var(--white);font-weight:700;font-size:12.5px}
  .social{position:absolute;top:727px;left:82px;display:flex;gap:13px}
  .social span{width:37px;height:37px;border-radius:5px;background:#8a8a8a}

  /* Back */
  .indicia{position:absolute;left:17px;top:32px;width:48px;height:58px;background:var(--white);display:flex;align-items:center;justify-content:center}
  .indicia p{transform:rotate(90deg);font:700 7px/1.05 Arial,sans-serif;text-align:center;color:var(--ink);white-space:nowrap}
  .recipient{position:absolute;left:87px;top:32px;width:66px;height:130px;background:#f2f2f2;border:1px solid #999;display:flex;align-items:center;justify-content:center}
  .recipient p{transform:rotate(-90deg);font-size:11.5px;line-height:1.15;color:var(--ink);white-space:nowrap}
  .address-box{position:absolute;left:126px;top:177px;width:126px;height:227px;background:var(--white);border-radius:18px}
  .address-box i{position:absolute;top:20px;bottom:20px;width:1px;background:#9a9a9a}
  .to{position:absolute;left:97px;top:360px;color:var(--white);font-size:12px;transform:rotate(-90deg)}
  .contact-card{position:absolute;left:45px;top:424px;width:207px;height:364px;background:var(--red);border-top-left-radius:22px}
  .contact-list{position:absolute;left:12px;top:16px;writing-mode:vertical-rl;transform:rotate(180deg);color:var(--white);font-size:11.5px;line-height:1.25;height:182px}
  .contact-list li{list-style:none;margin-left:9px;display:flex;align-items:center;gap:6px}
  .contact-list .heading{font-style:italic;font-weight:600;font-size:12.5px;margin-left:2px}
  .contact-list .phone{font-weight:700;font-size:13px}
  .contact-list svg{flex:none}
  .card-brand{position:absolute;left:16px;top:206px;width:160px;height:136px;background:var(--white);box-shadow:2px 2px 4px rgba(0,0,0,.4);display:flex;align-items:center;justify-content:center}
  .card-brand p{transform:rotate(-90deg);font-weight:600;font-size:13px;color:var(--ink);white-space:nowrap;text-align:center;line-height:1.2}
  .deadline{position:absolute;left:280px;top:768px;z-index:3;transform-origin:0 0;transform:rotate(-90deg);white-space:nowrap;color:var(--white);font:italic 700 14.5px/20px "Open Sans",Arial,sans-serif}

  /* Front */
  .front-photo{position:absolute;left:0;top:220px;width:343px;height:417px;background:linear-gradient(180deg,var(--photo-sky),var(--photo-green) 30%,var(--photo-brown) 65%,#8c7a56)}
  .front-brand{position:absolute;left:0;top:0;width:343px;height:280px;background:var(--white);border-radius:0 0 50% 50% / 0 0 36% 36%;box-shadow:0 6px 10px rgba(0,0,0,.45);display:flex;flex-direction:column;align-items:center;justify-content:center;gap:10px}
  .front-brand .name{font-weight:600;font-size:21px;color:var(--ink);text-align:center;line-height:1.2}
  .front-brand .mark{width:22px;height:22px;background:var(--ink)}
  .tagline-band{position:absolute;top:637px;left:0;width:343px;height:25px;background:var(--red);color:var(--white);font:italic 700 12px/25px "Open Sans",Arial,sans-serif;text-align:center}
  .call{position:absolute;top:682px;width:100%;text-align:center;color:var(--white);font:700 23px "Roboto Condensed",Arial,sans-serif;letter-spacing:.5px}
  .web{position:absolute;top:716px;width:100%;text-align:center;color:var(--white);font:700 17px "Roboto Condensed",Arial,sans-serif;letter-spacing:1px}
  .premier{position:absolute;top:763px;width:100%;text-align:center;color:var(--white);font-size:12px}
</style>
</head>
<body>
  <div class="panel-label" style="left:184px">Back flap</div>
  <div class="panel-label" style="left:482px">Back</div>
  <div class="panel-label" style="left:836px">Front</div>

  <main class="brochure">
    <section class="panel panel--flap">
      <h2 class="youth-title">Youth Hunts</h2>
      <p class="youth-sub">Fully Outfitted Muzzleloader/Rifle Elk</p>
      <p class="youth-price">($3,500)</p>
      <p class="youth-copy">Includes 5 full days of guiding (2 hunters/guide max), game retrieval, field transportation, field pictures, field caping of animal to atlas joint, wall tent accommodations (no cost upgrade to lodge accommodations per outfitters discretion / availability), breakfast, lunch, dinner, stoves, firewood, cots, sleeping pad, shower tent, latrine facility, lanterns, tables, chairs. 1/1 guide service may be added at the rates specified below.</p>
      <dl class="rates">
        <div class="rate"><dt>Youth Elk Rate</dt><dd>: $ 91 / 5780 (5 days)</dd></div>
        <div class="rate"><dt>Youth Mule Deer Rate</dt><dd>: $ 3,800 (5 days)<br>: $ 4,400 (7 days)</dd></div>
        <div class="rate"><dt>Youth Turkey Rate</dt><dd><p>: Fully Outfitted 3 day spring turkey hunt is $1,000/ person.</p><p style="margin-top:4px">: Non-hunting guest rate is $100/ day</p></dd></div>
      </dl>
      <div class="photo-strip">
        <div class="photo photo--turkey" role="img" aria-label="Young hunter kneeling behind a harvested wild turkey with fanned tail"></div>
        <div class="photo photo--youth-elk" role="img" aria-label="Young hunter standing beside a bull elk among pine trees"></div>
      </div>
      <h3 class="connect-title">Get Connected</h3>
      <div class="social" aria-label="Social media links"><span></span><span></span><span></span><span></span></div>
    </section>

    <section class="panel panel--back">
      <div class="indicia"><p>PRSRT STD<br>ECRWSS<br>U.S.POSTAGE<br>PAID<br>EDDM Retail</p></div>
      <div class="recipient"><p>Local<br>Postal Customer</p></div>
      <div class="address-box"><i style="left:26px"></i><i style="left:54px"></i><i style="left:82px"></i></div>
      <span class="to">To,</span>
      <div class="contact-card">
        <ul class="contact-list">
          <li class="heading">Contact Us:</li>
          <li><svg width="10" height="10" viewBox="0 0 10 10"><path d="M5 0 10 5H8.5V10H6V7H4V10H1.5V5H0Z" fill="#fff"/></svg>4820 Pinon Ridge Rd NE<br>Albuquerque, NM 87111.</li>
          <li class="phone"><svg width="11" height="11" viewBox="0 0 12 12"><circle cx="6" cy="6" r="5.5" fill="none" stroke="#fff"/><path d="M4 3.5 5 5 4.5 5.8Q5.5 7 6.3 7.5L7 7 8.5 8 7.8 9Q5 8.5 3.2 4.5Z" fill="#fff"/></svg>(505) 555-0142</li>
          <li><svg width="11" height="11" viewBox="0 0 12 12"><circle cx="6" cy="6" r="5.5" fill="none" stroke="#fff"/><rect x="3" y="4" width="6" height="4" fill="none" stroke="#fff" stroke-width=".8"/><path d="M3 4 6 6.5 9 4" fill="none" stroke="#fff" stroke-width=".8"/></svg>info@highmesaguides.example</li>
          <li><svg width="11" height="11" viewBox="0 0 12 12"><circle cx="6" cy="6" r="5.5" fill="none" stroke="#fff"/><ellipse cx="6" cy="6" rx="2.3" ry="5.5" fill="none" stroke="#fff" stroke-width=".8"/><path d="M.5 6H11.5" stroke="#fff" stroke-width=".8"/></svg>www.highmesaguides.example</li>
        </ul>
        <div class="card-brand"><p>Ridgeway Pack<br>Outfitters</p></div>
      </div>
      <p class="deadline">Give us a call before the draw deadline to book the best hunt of your life!</p>
    </section>

    <section class="panel panel--front">
      <div class="front-photo" role="img" aria-label="Hunter kneeling behind a large harvested bull elk on a grassy hillside with pines"></div>
      <div class="front-brand">
        <span class="mark"></span>
        <p class="name">Ridgeway Pack<br>Outfitters</p>
      </div>
      <p class="tagline-band">Turning dreams into reality, one trophy at a time!</p>
      <p class="call">Call: (505) 555-0142</p>
      <p class="web">www.highmesaguides.example</p>
      <p class="premier">New Mexico's Premier Outfitter</p>
    </section>
  </main>
</body>
</html>
```